Work Van Graphics Design

Use the attached logo and design a work van.  The van should be orange (the same orange in the attached logo) and the logo and text will be white.  I want the text to be big and bold, the same hight as the graphic in the logo.  The text should be "BRAMLEY HOUSE CREW'S" instead of just Bramley.
The other text that needs to be on the van somewhere:
www.BramleyHouseCrew.example
614-555-0182
Roofing
Plumbing
Water Restoration
Carpet Cleaning
Window Cleaning
HVAC

```html
<!DOCTYPE html>
<html lang="en">
<head>
<meta charset="utf-8">
<title>Bramley House Crew's – Work Van Graphics</title>
<link rel="stylesheet" href="https://fonts.googleapis.com/css2?family=Lato:wght@400;700&display=swap">
<style>
  :root {
    --bg: #efefef;
    --shadow: #d9d9d9;
    --van-white: #f7f7f7;
    --orange: #ec8235;
    --orange-dark: #d8682e;
    --orange-light: #f6c6a0;
    --ink: #3c3a3a;
    --white: #ffffff;
    --glass: #6b7475;
    --trim: #2a2a2a;
    --tyre: #1c1c1c;
    --rim: #d6d6d6;
    --hub: #454545;
    --tail: #b3241e;
  }
  html, body {
    margin: 0;
    width: 1200px;
    height: 800px;
    overflow: hidden;
    background: var(--bg);
  }
  .van-artwork { display: block; width: 1200px; height: 800px; }
  .brand-name { font-family: "Lato", sans-serif; font-weight: 700; fill: var(--white); font-size: 20px; }
  .brand-web { font-family: "Lato", sans-serif; font-weight: 400; fill: var(--white); font-size: 7px; letter-spacing: 1.5px; }
  .brand-phone { font-family: "Lato", sans-serif; font-weight: 400; fill: var(--white); font-size: 10px; letter-spacing: 1.3px; }
  .service { font-family: "Lato", sans-serif; font-weight: 400; fill: var(--ink); font-size: 15px; font-variant: small-caps; letter-spacing: 1.6px; }
  .bullet { fill: var(--ink); }
</style>
</head>
<body>
<svg class="van-artwork" viewBox="0 0 1200 800" xmlns="http://www.w3.org/2000/svg">
  <defs>
    <clipPath id="van-body">
      <path d="M150,462 Q152,440 175,432 L300,405 Q330,398 345,392 L430,320 Q470,290 520,278 Q580,266 640,264 L995,267 L1003,272 L1000,280 Q1012,320 1022,390 L1026,500 L1028,556 L150,556 Z"/>
    </clipPath>
    <linearGradient id="tone-faucet" x1="0" y1="0" x2="0" y2="1">
      <stop offset="0" stop-color="#e6e6e6"/><stop offset="1" stop-color="#b9b9b9"/>
    </linearGradient>
    <linearGradient id="tone-carpet" x1="0" y1="0" x2="1" y2="1">
      <stop offset="0" stop-color="#dfe9ee"/><stop offset="1" stop-color="#a9bfcc"/>
    </linearGradient>
    <linearGradient id="tone-window" x1="0" y1="0" x2="0" y2="1">
      <stop offset="0" stop-color="#9fb3c6"/><stop offset="1" stop-color="#6f8399"/>
    </linearGradient>
  </defs>

  <ellipse class="ground-shadow" cx="595" cy="594" rx="470" ry="14" fill="var(--shadow)"/>

  <g class="van-side" clip-path="url(#van-body)">
    <rect class="base-white" x="100" y="240" width="960" height="340" fill="var(--van-white)"/>
    <path class="sweep-dark" d="M624,262 Q600,450 355,559 L446,559 Q612,460 636,262 Z" fill="var(--orange-dark)"/>
    <path class="sweep-main" d="M644,262 Q626,470 462,559 L1060,559 L1060,250 Z" fill="var(--orange)"/>
    <path class="sweep-line" d="M640,262 Q620,465 455,559" fill="none" stroke="var(--white)" stroke-width="6"/>
    <polygon class="panel-accent" points="689,357 765,357 928,559 796,559" fill="var(--orange-light)" opacity="0.55"/>
    <polygon class="panel-accent" points="860,380 1030,380 1030,510" fill="var(--orange-light)" opacity="0.45"/>
  </g>

  <path class="side-window" d="M340,408 L408,320 L571,305 L569,400 Z" fill="var(--glass)" stroke="var(--trim)" stroke-width="4" stroke-linejoin="round"/>
  <line class="window-pillar" x1="390" y1="346" x2="388" y2="405" stroke="var(--trim)" stroke-width="4"/>
  <rect class="mirror" x="393" y="364" width="30" height="36" rx="8" fill="var(--trim)"/>
  <rect class="door-handle" x="525" y="433" width="40" height="6" rx="3" fill="var(--trim)"/>
  <rect class="side-indicator" x="344" y="434" width="28" height="6" rx="3" fill="var(--trim)"/>
  <rect class="side-rub-strip" x="386" y="474" width="370" height="6" rx="3" fill="var(--trim)"/>
  <rect class="tail-light" x="1005" y="403" width="21" height="59" rx="4" fill="var(--tail)"/>

  <path class="front-bumper" d="M143,470 L240,467 Q232,520 230,559 L150,559 Q143,540 143,520 Z" fill="var(--trim)"/>
  <path class="rear-bumper" d="M934,500 L1035,498 Q1045,505 1043,520 L1040,545 L940,549 Z" fill="var(--trim)"/>

  <g class="wheel front-wheel">
    <circle cx="288" cy="541" r="68" fill="var(--trim)"/>
    <circle cx="288" cy="541" r="59" fill="var(--tyre)"/>
    <circle cx="288" cy="541" r="41" fill="var(--rim)"/>
    <circle cx="288" cy="541" r="13" fill="var(--hub)"/>
  </g>
  <g class="wheel rear-wheel">
    <circle cx="867" cy="541" r="68" fill="var(--trim)"/>
    <circle cx="867" cy="541" r="59" fill="var(--tyre)"/>
    <circle cx="867" cy="541" r="41" fill="var(--rim)"/>
    <circle cx="867" cy="541" r="13" fill="var(--hub)"/>
  </g>

  <g class="service-photos">
    <circle cx="673" cy="321" r="47" fill="var(--white)"/>
    <circle cx="673" cy="321" r="39" fill="url(#tone-faucet)" role="img" aria-label="Photo of a chrome bathroom faucet"/>
    <circle cx="632" cy="418" r="46" fill="var(--white)"/>
    <circle cx="632" cy="418" r="38" fill="url(#tone-carpet)" role="img" aria-label="Photo of a technician cleaning carpet"/>
    <circle cx="569" cy="507" r="46" fill="var(--white)"/>
    <circle cx="569" cy="507" r="38" fill="url(#tone-window)" role="img" aria-label="Photo of a window cleaner on ropes"/>
  </g>

  <g class="brand-block">
    <rect x="774" y="285" width="14" height="14" fill="var(--white)"/>
    <text class="brand-name" x="796" y="300">BRAMLEY</text>
    <text class="brand-name" x="796" y="324">HOUSE CREW'S</text>
    <text class="brand-web" x="837" y="339" text-anchor="middle">WWW.BRAMLEYHOUSECREW.EXAMPLE</text>
    <text class="brand-phone" x="837" y="353" text-anchor="middle">614-555-0182</text>
  </g>

  <g class="service-list">
    <circle class="bullet" cx="734" cy="384" r="4"/>
    <text class="service" x="744" y="389">Carpet Cleaning</text>
    <circle class="bullet" cx="895" cy="384" r="4"/>
    <text class="service" x="905" y="389">Roofing</text>
    <circle class="bullet" cx="714" cy="409" r="4"/>
    <text class="service" x="724" y="414">Water Restoration</text>
    <circle class="bullet" cx="883" cy="409" r="4"/>
    <text class="service" x="893" y="414">Plumbing</text>
    <circle class="bullet" cx="699" cy="436" r="4"/>
    <text class="service" x="709" y="441">Window Cleaning</text>
    <circle class="bullet" cx="867" cy="436" r="4"/>
    <text class="service" x="877" y="441">HVAC</text>
  </g>
</svg>
</body>
</html>
```